Business Card Design REAL ESTATE SALES PLEASE DESIGN MY CARD 2COLOR CARD WITH RED AS THE DOMINANT

MOOR PINE REALTY
TorVHA Lic# 04827316
WALTER " WALT " KOVIC Tel 510 555-0142
TorVHA Lic# 00762408 Fax 510 555-0187
Email: walt@waltkovic.example Cell 510 555-0163
48610 FERNHILL COURT HARLOW CITY, CA 94999

Business

WALTER " WALT " KOVIC
TEL: 510 555-0142 FAX 510 555-0187
Address: 48610 Fernhill Court Harlow City , CA
EMAIL ADDRESS: walt@waltkovic.example

```html
<!DOCTYPE html>
<html lang="en">
<head>
<meta charset="utf-8">
<title>Moor Pine Realty – Business Card</title>
<link href="https://fonts.googleapis.com/css2?family=Questrial&display=swap" rel="stylesheet">
<style>
  :root {
    --brand-red: #e31e2a;
    --brand-red-dark: #c9151f;
    --ink: #2a2a2a;
    --paper: #ffffff;
    --backdrop: #ecebe8;
    --edge: rgba(0, 0, 0, 0.12);
  }
  * { box-sizing: border-box; margin: 0; padding: 0; }
  html, body {
    width: 714px;
    height: 1200px;
    overflow: hidden;
    background: var(--backdrop);
    font-family: "Questrial", sans-serif;
  }
  .sheet {
    width: 714px;
    height: 1200px;
    display: flex;
    flex-direction: column;
    align-items: center;
    justify-content: space-around;
    padding: 80px 0;
  }
  .card {
    width: 600px;
    height: 343px;
    position: relative;
    box-shadow: 0 2px 10px var(--edge);
  }
  .card--front { background: var(--paper); color: var(--ink); }
  .card--back {
    background: linear-gradient(135deg, var(--brand-red) 0%, var(--brand-red-dark) 100%);
    color: var(--paper);
    display: flex;
    align-items: center;
    justify-content: center;
  }
  .brand {
    display: flex;
    align-items: center;
    gap: 12px;
    color: var(--brand-red);
    font-size: 19px;
    letter-spacing: 1.5px;
    white-space: nowrap;
  }
  .brand__mark {
    width: 22px;
    height: 22px;
    background: currentColor;
    flex: none;
  }
  .card--front .brand {
    position: absolute;
    left: 36px;
    top: 220px;
  }
  .card--back .brand {
    color: var(--paper);
    font-size: 36px;
    letter-spacing: 3px;
    gap: 18px;
  }
  .card--back .brand__mark { width: 38px; height: 38px; }
  .contact {
    position: absolute;
    left: 270px;
    top: 62px;
    width: 310px;
  }
  .contact__name {
    font-size: 22px;
    letter-spacing: 0.5px;
    white-space: nowrap;
  }
  .contact__licence {
    color: var(--brand-red);
    font-size: 13px;
    margin-top: 6px;
    margin-bottom: 22px;
  }
  .contact__row {
    display: flex;
    gap: 26px;
    font-size: 13px;
    margin-bottom: 12px;
  }
  .contact__item {
    display: flex;
    align-items: center;
    gap: 7px;
    white-space: nowrap;
  }
  .icon { width: 12px; height: 12px; fill: var(--brand-red); flex: none; }
</style>
</head>
<body>
<main class="sheet">
  <section class="card card--front" aria-label="Card front">
    <div class="brand">
      <span class="brand__mark"></span>
      <span class="brand__name">MOOR PINE REALTY</span>
    </div>
    <div class="contact">
      <h1 class="contact__name">WALTER " WALT " KOVIC</h1>
      <p class="contact__licence">TorVHA Lic# 00762408</p>
      <div class="contact__row">
        <span class="contact__item">
          <svg class="icon" viewBox="0 0 12 12"><path d="M2.5 1h2l1 3-1.5 1a7 7 0 0 0 3 3l1-1.5 3 1v2c0 .6-.4 1-1 1A10 10 0 0 1 1.5 2c0-.6.4-1 1-1z"/></svg>
          510 555-0142
        </span>
        <span class="contact__item">
          <svg class="icon" viewBox="0 0 12 12"><rect x="3" y="1" width="6" height="3"/><rect x="1" y="4.5" width="10" height="4.5" rx="1"/><rect x="3" y="8" width="6" height="3"/></svg>
          510 555-0187
        </span>
      </div>
      <div class="contact__row">
        <span class="contact__item">
          <svg class="icon" viewBox="0 0 12 12"><path d="M6 0.5a4 4 0 0 0-4 4c0 3 4 7 4 7s4-4 4-7a4 4 0 0 0-4-4zm0 5.7a1.7 1.7 0 1 1 0-3.4 1.7 1.7 0 0 1 0 3.4z"/></svg>
          48610 Fernhill Court Harlow City , CA
        </span>
      </div>
      <div class="contact__row">
        <span class="contact__item">
          <svg class="icon" viewBox="0 0 12 12"><path d="M1 2.5h10v7H1z M1 2.5l5 4 5-4" fill="var(--brand-red)" stroke="#fff" stroke-width="0.8"/></svg>
          walt@waltkovic.example
        </span>
      </div>
    </div>
  </section>

  <section class="card card--back" aria-label="Card back">
    <div class="brand">
      <span class="brand__mark"></span>
      <span class="brand__name">MOOR PINE REALTY</span>
    </div>
  </section>
</main>
</body>
</html>
```